Letterhead designs for Property Management firm

Would like to see some different letterhead/envelope designs We are a residential property management company. We would like to see designs that utilize blue/grays/black

```html
<!DOCTYPE html>
<html lang="en">
<head>
<meta charset="UTF-8">
<title>Ridgeview Property Management – Letterhead</title>
<link rel="stylesheet" href="https://fonts.googleapis.com/css2?family=Arimo:wght@400;700&family=Exo:wght@400&display=swap">
<style>
  :root {
    --brand-blue: #0353a4;
    --rail-grey: #d6d6d6;
    --rail-shade: #9a9a9a;
    --ink: #111111;
    --page-edge: #3a3a3a;
    --canvas: #ffffff;
    --sketch-light: #f4f4f4;
    --sketch-mid: #dcdcdc;
  }
  * { box-sizing: border-box; margin: 0; padding: 0; }
  html, body {
    width: 1200px; height: 1200px; overflow: hidden;
    background: var(--canvas);
  }
  .canvas {
    position: relative; width: 1200px; height: 1200px;
    border: 1px solid #bdbdbd; background: var(--canvas);
  }
  .letterhead {
    position: absolute; left: 199px; top: 34px;
    width: 802px; height: 1132px;
    border: 1px solid var(--page-edge); background: #fff;
    overflow: hidden;
  }
  .letterhead__art { position: absolute; inset: 0; }
  .brand {
    position: absolute; left: 119px; top: 62px;
    display: flex; align-items: center; gap: 10px;
    font-family: "Arimo", Arial, sans-serif; font-weight: 700;
    color: var(--brand-blue);
  }
  .brand__mark { width: 22px; height: 22px; background: var(--brand-blue); }
  .brand__name {
    font-size: 19px; line-height: 1.15; letter-spacing: 0.5px;
    text-transform: uppercase;
  }
  .tagline {
    position: absolute; left: 459px; top: 48px;
    font-family: "Exo", "Arimo", sans-serif; font-size: 14.5px;
    letter-spacing: 0.6px; color: var(--ink);
  }
  .city-sketch {
    position: absolute; left: 343px; top: 910px;
    width: 414px; height: 200px;
    background: linear-gradient(180deg, rgba(255,255,255,0) 0%, var(--sketch-light) 35%, var(--sketch-mid) 100%);
  }
  .contact {
    position: absolute; left: 59px; top: 943px;
    list-style: none;
    font-family: "Arimo", Arial, sans-serif; font-size: 14.5px; color: var(--ink);
  }
  .contact__item {
    display: flex; align-items: center; gap: 8px;
    height: 40px;
  }
  .contact__icon {
    width: 34px; height: 34px; flex: none;
    border-radius: 50%; background: var(--brand-blue);
    box-shadow: 0 0 0 3px #fff, 0 0 0 4px #e2e2e2;
    display: flex; align-items: center; justify-content: center;
  }
  .contact__icon svg { width: 20px; height: 20px; }
  .contact__text { line-height: 1.0; }
</style>
</head>
<body>
<div class="canvas">
  <div class="letterhead">
    <svg class="letterhead__art" width="802" height="1132" viewBox="0 0 802 1132" aria-hidden="true">
      <!-- side rail -->
      <rect class="rail" x="42" y="0" width="30" height="1132" fill="var(--rail-grey)"/>
      <polygon points="29,271 42,246 42,271" fill="var(--rail-shade)"/>
      <polygon points="85,271 72,246 72,271" fill="var(--rail-shade)"/>
      <polygon points="29,827 42,852 42,827" fill="var(--rail-shade)"/>
      <polygon points="85,827 72,852 72,827" fill="var(--rail-shade)"/>
      <rect class="rail-band" x="29" y="271" width="56" height="556" fill="var(--brand-blue)"/>
      <!-- frame line -->
      <polyline points="447,42 769,42 769,1082 329,1082" fill="none" stroke="var(--brand-blue)" stroke-width="3"/>
      <circle cx="447" cy="42" r="7" fill="var(--brand-blue)"/>
      <circle cx="329" cy="1082" r="7" fill="var(--brand-blue)"/>
    </svg>

    <div class="brand">
      <span class="brand__mark"></span>
      <span class="brand__name">Ridgeview<br>Property Management</span>
    </div>

    <p class="tagline">Your Full Service Real Estate Company</p>

    <div class="city-sketch" role="img" aria-label="Light pencil sketch of a city skyline with towers and office blocks"></div>

    <ul class="contact">
      <li class="contact__item">
        <span class="contact__icon">
          <svg viewBox="0 0 20 20" fill="none" stroke="#fff" stroke-width="1.3"><circle cx="10" cy="10" r="8"/><ellipse cx="10" cy="10" rx="3.5" ry="8"/><line x1="2" y1="10" x2="18" y2="10"/><line x1="3.5" y1="6" x2="16.5" y2="6"/><line x1="3.5" y1="14" x2="16.5" y2="14"/></svg>
        </span>
        <span class="contact__text">www.ridgeview-homes.com</span>
      </li>
      <li class="contact__item">
        <span class="contact__icon">
          <svg viewBox="0 0 20 20" fill="none" stroke="#fff" stroke-width="1.4"><rect x="2.5" y="5" width="15" height="10"/><polyline points="2.5,5 10,11 17.5,5"/><line x1="2.5" y1="15" x2="8" y2="10"/><line x1="17.5" y1="15" x2="12" y2="10"/></svg>
        </span>
        <span class="contact__text">mcarter.ridgeview@mail.com</span>
      </li>
      <li class="contact__item">
        <span class="contact__icon">
          <svg viewBox="0 0 20 20" fill="#fff"><path d="M5 3.5l2.6-.4 1.4 3.4-1.7 1.3c.8 1.8 2.1 3.1 3.9 3.9l1.3-1.7 3.4 1.4-.4 2.6c-.2 1-1 1.6-2 1.5C8.6 15 5 11.4 4.5 5.5c-.1-1 .5-1.8 1.5-2z"/></svg>
        </span>
        <span class="contact__text">+1 555-014-2290</span>
      </li>
      <li class="contact__item">
        <span class="contact__icon">
          <svg viewBox="0 0 20 20" fill="#fff"><path d="M10 2a5.5 5.5 0 0 0-5.5 5.5C4.5 11.5 10 18 10 18s5.5-6.5 5.5-10.5A5.5 5.5 0 0 0 10 2zm0 7.8a2.3 2.3 0 1 1 0-4.6 2.3 2.3 0 0 1 0 4.6z"/></svg>
        </span>
        <span class="contact__text">4820 Harbor Crest Ave<br>90210 Fairmont, California</span>
      </li>
    </ul>
  </div>
</div>
</body>
</html>
```